Stationery Design Project

Brivan-Holt Consultants is interim management company. We are specialized in finding the best Finance and IT consultants for our clients when they require additional resources on an interim basis for projects or special situations. We are flexible in our approach and we always seek to maximize the benefits for our clients as well as our consultants.

We are looking for a design of our letterhead, general stationery and business cards using the company name. The design will also be found on our coming web pages.
Updates

Please also create a logo for Brivan-Holt Consultants which expresses that we want to match the best finance and IT people to our customers projects

Target Market(s)

Larger and mid sized companies (all sectors), as well as highly skilled Finance & IT professionals/consultants

Industry/Entity Type

Business

Requirements
Must have
• Brivan-Holt Consultants
We are expecting that 'Brivan-Holt' will be on the first line and 'Consultants' on a second line.
Please also indicate style of the letters for our address/phone and mail details. Our current address is:
Tarnvoldgade 9,
2870 Kalsbro
Danmark
Mobile: +45 XX XX XX XX Mail: xx@brivan-holt.dk

```html
<!DOCTYPE html>
<html lang="en">
<head>
<meta charset="utf-8">
<title>Brivan-Holt Consultants – Business Cards</title>
<link rel="stylesheet" href="https://fonts.googleapis.com/css2?family=Inter:wght@700&display=swap">
<style>
  :root {
    --page-bg: #000000;
    --card-blue-center: #2553b6;
    --card-blue-edge: #1b3c8e;
    --ink-white: #ffffff;
    --card-width: 577px;
    --card-height: 370px;
  }
  * { margin: 0; padding: 0; box-sizing: border-box; }
  html, body {
    width: 1200px;
    height: 900px;
    overflow: hidden;
    background: var(--page-bg);
  }
  .stationery {
    position: relative;
    width: 1200px;
    height: 900px;
    font-family: "Inter", Arial, sans-serif;
    font-weight: 700;
    color: var(--ink-white);
  }
  .business-card {
    position: absolute;
    top: 181px;
    width: var(--card-width);
    height: var(--card-height);
    background: radial-gradient(ellipse at 45% 25%, var(--card-blue-center) 0%, var(--card-blue-edge) 85%);
    overflow: hidden;
  }
  .business-card--front { left: 20px; }
  .business-card--back { left: 607px; }

  /* Front: centred wordmark */
  .front-wordmark {
    position: absolute;
    left: 0;
    right: 0;
    top: 136px;
    text-align: center;
  }
  .front-wordmark__name {
    display: block;
    font-size: 48px;
    line-height: 1;
    letter-spacing: 0.01em;
    text-transform: uppercase;
  }
  .front-wordmark__tagline {
    display: block;
    margin-top: 14px;
    font-size: 15px;
    line-height: 1;
    letter-spacing: 0.45em;
    padding-left: 0.45em;
    text-transform: uppercase;
  }

  /* Back: large wordmark and contact details */
  .back-wordmark {
    position: absolute;
    left: 26px;
    top: 40px;
  }
  .back-wordmark__name {
    display: block;
    font-size: 66px;
    line-height: 1;
    letter-spacing: -0.01em;
    text-transform: uppercase;
  }
  .back-wordmark__tagline {
    display: block;
    margin-top: 14px;
    font-size: 30px;
    line-height: 1;
    letter-spacing: 0.28em;
    text-transform: uppercase;
  }
  .contact-details {
    position: absolute;
    left: 344px;
    top: 259px;
    font-style: normal;
    font-size: 15px;
    line-height: 17.5px;
  }
  .contact-details__line { display: block; white-space: nowrap; }
</style>
</head>
<body>
<main class="stationery">
  <section class="business-card business-card--front" aria-label="Business card front">
    <div class="front-wordmark">
      <span class="front-wordmark__name">Brivan-Holt</span>
      <span class="front-wordmark__tagline">Consultants</span>
    </div>
  </section>

  <section class="business-card business-card--back" aria-label="Business card back">
    <div class="back-wordmark">
      <span class="back-wordmark__name">Brivan-Holt</span>
      <span class="back-wordmark__tagline">Consultants</span>
    </div>
    <address class="contact-details">
      <span class="contact-details__line">Tarnvoldgade 9</span>
      <span class="contact-details__line">2870 Kalsbro</span>
      <span class="contact-details__line">Danmark</span>
      <span class="contact-details__line">Mobile: +45 XX XX XX XX</span>
      <span class="contact-details__line">Mail: xx@brivan-holt.dk</span>
    </address>
  </section>
</main>
</body>
</html>
```